International Petrochemical business needs a web design for Clearway Desk system

We need a web design for a "Clearway Desk" system for an international petrochemical company. The web site is used internally within the company. It is hosted by an internal department which provides government permit request service for other departments.

We would like to see designs of two pages using color light blue. (home page, internal page as attached).
Home Page:
1. Header has a background image and small animation. Header on home page can be taller than the header of the internal page.
2. Layout as attached.

Internal Page:
1. Header can use the same background image as the home page and can be shorter to utilize the page for content.
2. The blue icon behind every captions represent an icon. When user move mouse over this icon, it displays the caption in Thai language as a tooltip. This icon needs to be redesign.

The final design should communicate the followings:
- Excellent service provided system in terms of time and accurary
- Rapid growth of business via building petrochemical refinery plant

For Internal Page, the blue circle behind every captions represent an icon. When mouse over this icon, a tool tip showing the caption in Thai language is shown. Please also design this icon..

There are more feedbacks from customer as followed:

1. Banner should consists of 
    1.1 "Approved" stamp on paper
    1.2 An image of Garuda. It is used on every government documents in Thailand
    1.3 Image of petrochemical plant
2. Each menu item (Home, Permit, Search, etc) should have different colors. Drop down menu will use the same color as its parent menu item.
3. Overall tone of the web page should be light blue with background of the body the web page in white
4. "New Request" button should use green color with icon on it
5. Table header of each box in the body of the page should use dark blue background with text in white

Please kindly submit your revisions.
Thank you.

Reason: We get some late feedbacks from customers which was just updated to all designers.

• 1. Design for 1024x768 screen resolution
2. Use light blue theme
3. Background of header where the company logo is must have white background

```html
<!DOCTYPE html>
<html lang="en">
<head>
<meta charset="utf-8">
<title>Norvale Petrochemical – Clearway Desk</title>
<link rel="stylesheet" href="https://fonts.googleapis.com/css2?family=Source+Sans+3:wght@400;600;700&family=Sarabun:wght@400&display=swap">
<style>
  :root{
    --navy:#1e2a6c;
    --ink:#111;
    --sky:#1db2ea;
    --sky-light:#67cdf3;
    --panel:#e9f1f7;
    --panel-top:#f3f7fa;
    --table-head:#1f3d7a;
    --white:#fff;
    --green:#3aa845;
    --green-dark:#2a8a35;
    --dot-red:#e2464f;
    --dot-yellow:#f1e31e;
    --menu-home:#1e2a6c;
    --menu-permits:#0e8fc9;
    --menu-search:#16a39a;
    --menu-report:#6b4fb8;
    --menu-admin:#e0822a;
    --menu-help:#3aa845;
  }
  *{box-sizing:border-box;margin:0;padding:0}
  html,body{width:1099px;height:1200px;overflow:hidden}
  body{
    position:relative;
    font-family:"Source Sans 3","Sarabun",sans-serif;
    color:var(--ink);
    background:linear-gradient(180deg,#eef1f4 0,#f4f6f8 420px,#e6eef4 820px,#b9d3e7 1000px,#8fb4d6 1200px);
  }
  .plant-backdrop{
    position:absolute;left:0;right:0;top:1000px;height:200px;
    background:
      radial-gradient(ellipse at 20% 95%,rgba(235,245,255,.65),transparent 45%),
      radial-gradient(ellipse at 70% 90%,rgba(220,238,255,.55),transparent 50%),
      linear-gradient(180deg,rgba(170,200,228,0) 0,#7fa9d0 55%,#6b98c6 100%);
  }
  .brand{position:absolute;left:38px;top:24px;height:50px;display:flex;align-items:center;gap:10px}
  .brand-mark{width:34px;height:34px;border-radius:50%;background:var(--sky)}
  .brand-name{font-weight:700;font-size:20px;line-height:22px;color:var(--sky);letter-spacing:.5px}

  .main-nav{
    position:absolute;left:0;top:94px;width:1099px;height:52px;
    background:linear-gradient(180deg,#7ad6f6 0,#3fc0ee 45%,#20b3e9 100%);
  }
  .main-nav a{
    position:absolute;top:0;height:52px;padding:12px 10px 0;
    font-size:20.5px;color:var(--navy);text-decoration:none;
    border-bottom:5px solid var(--item);
  }
  .main-nav a.active{background:var(--item);color:var(--white)}
  .dropdown{
    position:absolute;left:120px;top:146px;width:189px;height:101px;
    background:var(--menu-permits);padding:14px 0 0 14px;z-index:2;
  }
  .dropdown a{display:block;color:var(--white);font-size:15px;line-height:26px;text-decoration:none}

  .hero{
    position:absolute;left:13px;top:153px;width:1071px;height:272px;border-radius:4px;
    background:
      radial-gradient(ellipse at 45% 60%,rgba(255,205,120,.55),transparent 35%),
      radial-gradient(ellipse at 75% 50%,rgba(255,190,110,.35),transparent 30%),
      linear-gradient(180deg,#93a8c4 0,#6f87a8 35%,#3d4d66 70%,#5c6470 100%);
  }
  .hero-arrows{position:absolute;left:981px;top:368px}

  .panel{
    position:absolute;border-radius:4px;
    background:linear-gradient(180deg,var(--panel-top),var(--panel));
  }
  .panel h2{position:absolute;left:18px;top:12px;font-weight:400;font-size:21.5px;color:var(--navy)}
  .panel .rule{position:absolute;left:0;right:0;top:51px;height:1px;background:#fff}
  .table-head{
    position:absolute;left:0;right:2px;top:55px;height:35px;
    background:var(--table-head);color:var(--white);font-size:14.5px;
  }
  .table-head span,.row span{position:absolute;white-space:nowrap}
  .table-head span{top:8px}
  .row{position:absolute;left:0;right:0;height:24px;font-size:14.5px}
  .row .thai{font-family:"Sarabun",sans-serif;font-size:13px}
  .pager{position:absolute;left:14px;bottom:12px;display:flex;gap:3px}
  .pager i{width:7px;height:7px;background:var(--sky)}
  .pager i:first-child{background:var(--sky-light)}
  .status-dot{position:absolute;width:12px;height:11px;border-radius:50%}

  .new-request{
    position:absolute;left:553px;top:835px;width:521px;height:47px;border-radius:4px;
    background:linear-gradient(180deg,#4cbf58,var(--green-dark));
    color:var(--white);font-weight:600;font-size:22px;text-decoration:none;
    display:flex;align-items:center;justify-content:center;gap:10px;
  }

  .site-footer a{position:absolute;top:1114px;font-size:14.5px;color:var(--ink);text-decoration:none}
  .site-footer .page-code{position:absolute;top:1114px;left:1055px;font-size:14.5px}
</style>
</head>
<body>
  <div class="plant-backdrop" role="img" aria-label="Night view of refinery plant along the page foot"></div>

  <header>
    <div class="brand">
      <span class="brand-mark"></span>
      <span class="brand-name">NORVALE<br>PETROCHEMICAL</span>
    </div>
    <nav class="main-nav">
      <a style="left:28px;--item:var(--menu-home)">Home</a>
      <a class="active" style="left:120px;--item:var(--menu-permits)">Permits</a>
      <a style="left:225px;--item:var(--menu-search)">Search</a>
      <a style="left:324px;--item:var(--menu-report)">Report</a>
      <a style="left:422px;--item:var(--menu-admin)">Admin</a>
      <a style="left:519px;--item:var(--menu-help)">Help</a>
    </nav>
    <div class="dropdown">
      <a>Create New Permit</a>
      <a>Transfer Role</a>
      <a>Transfer Res. Person</a>
    </div>
    <div class="hero" role="img" aria-label="Petrochemical refinery plant lit up at dusk"></div>
    <svg class="hero-arrows" width="96" height="34" viewBox="0 0 96 34" aria-hidden="true">
      <circle cx="16" cy="17" r="14.5" fill="none" stroke="#fff" stroke-width="3"/>
      <path d="M19 11 L12 17 L19 23 Z" fill="#fff"/>
      <circle cx="56" cy="17" r="14.5" fill="none" stroke="#fff" stroke-width="3"/>
      <path d="M53 11 L60 17 L53 23 Z" fill="#fff"/>
    </svg>
  </header>

  <main>
    <section class="panel" style="left:20px;top:451px;width:522px;height:227px">
      <h2>New Requests</h2><div class="rule"></div>
      <div class="table-head"><span style="left:21px">Request No.</span><span style="left:173px">Requested Date</span><span style="left:324px">Branch</span></div>
      <div class="row" style="top:106px"><span style="left:21px">56-0003</span><span style="left:173px">20/4/2013</span><span style="left:324px">GC1</span></div>
      <div class="row" style="top:130px"><span style="left:21px">56-0004</span><span style="left:173px">21/4/2013</span><span style="left:324px">GC2</span></div>
      <div class="pager"><i></i><i></i><i></i><i></i></div>
    </section>

    <section class="panel" style="left:553px;top:451px;width:521px;height:227px">
      <h2>My Working Requests</h2><div class="rule"></div>
      <div class="table-head"><span style="left:27px">Request No.</span><span style="left:178px">Requested Date</span><span style="left:328px">Status</span></div>
      <div class="row" style="top:106px"><span style="left:27px">55-0200</span><span style="left:178px">25/3/2013</span><span style="left:328px">Waiting for process</span></div>
      <div class="row" style="top:130px"><span style="left:27px">55-0210</span><span style="left:178px">24/3/2013</span><span style="left:328px">In progress</span></div>
      <div class="row" style="top:154px"><span style="left:27px">55-0300</span><span style="left:178px">18/1/2013</span><span style="left:328px">Incomplete document</span></div>
      <div class="row" style="top:178px"><span style="left:27px">55-0301</span><span style="left:178px">18/1/2013</span><span style="left:328px">Cancel requested</span></div>
      <div class="pager" style="left:32px"><i></i><i></i><i></i><i></i></div>
    </section>

    <section class="panel" style="left:20px;top:686px;width:1054px;height:142px">
      <h2 style="top:6px">Expiring Permits</h2>
      <div class="rule" style="top:41px;right:500px"></div>
      <div class="table-head" style="top:41px;height:36px"><span style="left:21px">Permit No</span><span style="left:173px">Expire Date</span><span style="left:324px">Permit Name</span><span style="left:527px">Branch</span><span style="left:668px">Required Time (Day)</span><span style="left:862px">Due Date</span></div>
      <div class="row" style="top:85px"><span style="left:21px">AB56001</span><span style="left:173px">25/3/2013</span><span style="left:324px">Permit Name ###10</span><span style="left:527px">GC1</span><span style="left:668px">30</span><i class="status-dot" style="left:772px;top:3px;background:var(--dot-red);border:1px solid #b8343c"></i><span style="left:862px">-40</span></div>
      <div class="row" style="top:108px"><span style="left:21px">BIO5502</span><span style="left:173px">24/3/2013</span><span style="left:324px">Permit Name ###20</span><span style="left:527px">GC2</span><span style="left:668px">60</span><i class="status-dot" style="left:772px;top:6px;background:var(--dot-yellow);border:1px solid #c9b912"></i><span style="left:862px">15</span></div>
    </section>

    <section class="panel" style="left:20px;top:835px;width:522px;height:246px">
      <h2>My In Progress Requests</h2><div class="rule" style="top:50px"></div>
      <div class="table-head" style="top:52px;height:36px"><span style="left:21px">Request No.</span><span style="left:173px">Requested Date</span><span style="left:324px">Branch</span></div>
      <div class="row" style="top:94px"><span style="left:21px">56-00001</span><span style="left:173px">20/4/2013</span><span class="thai" style="left:324px">ระหว่างดำเนินการ</span></div>
      <div class="row" style="top:118px"><span style="left:21px">56-00002</span><span style="left:173px">21/4/2013</span><span class="thai" style="left:324px">รอดำเนินการ</span></div>
      <div class="pager"><i></i><i></i><i></i><i></i></div>
    </section>

    <a class="new-request">
      <svg width="22" height="22" viewBox="0 0 22 22" aria-hidden="true">
        <circle cx="11" cy="11" r="10" fill="none" stroke="#fff" stroke-width="2"/>
        <path d="M11 6 V16 M6 11 H16" stroke="#fff" stroke-width="2.4" stroke-linecap="round"/>
      </svg>
      NEW REQUEST
    </a>

    <section class="panel" style="left:553px;top:887px;width:521px;height:194px">
      <h2 style="top:10px">Recent Completed Requests</h2><div class="rule" style="top:52px"></div>
      <div class="table-head" style="top:54px;height:36px"><span style="left:27px">Request No.</span><span style="left:178px">Completed Date</span></div>
      <div class="row" style="top:96px"><span style="left:27px">55-0100</span><span style="left:178px">25/3/2013</span></div>
      <div class="row" style="top:120px"><span style="left:27px">55-0088</span><span style="left:178px">24/3/2013</span></div>
      <div class="row" style="top:144px"><span style="left:27px">55-0002</span><span style="left:178px">18/1/2013</span></div>
      <div class="pager" style="left:32px"><i></i><i></i><i></i><i></i></div>
    </section>
  </main>

  <footer class="site-footer">
    <a style="left:38px">Home</a>
    <a style="left:104px">Permits</a>
    <a style="left:180px">Search</a>
    <a style="left:251px">Report</a>
    <a style="left:322px">Admin</a>
    <a style="left:392px">Help</a>
    <span class="page-code">M1</span>
  </footer>
</body>
</html>
```